Web design for a Senior Home Care company

I want a web design for a home care company called Willowmere Home Care. What WHC does is send caregivers into people's homes to assist with daily living needs such as companionship, food preparation, cleaning, bathing, using the bathroom, etc. Most of the clients are seniors. The people deciding to use WHC are usually the 50 year old children of these senior citizens. Most visitors to the site will be women searching for this service for their parents.

The call to action is to inspire the website visitors to call us to set up an appointment to meet them in their home. The site design should inspire confidence in Willowmere Home Care to care for people's needs. We want to show the same attributes that a parent should have. Safety, Security and Loving Care.

Again, the goal of the site is to inspire and make it EASY for visitors to contact us either by phone call or through the website. The first choice is that they call us.

To help you with your ideas, In the attachments I've included different versions of our logo, a site map, examples of photos we might use and very rough draft of the website copy.

Target Market(s)

The customers will mostly be seniors. But, the people who will decide to use the company will the the 50 year old children of those seniors. Also, it is mostly women who are looking for help for their parents.

Industry/Entity Type

It Company

Number of Pages Required

5+ page

Requirements
Nice to have
• I want site visitors to easily be able to contact us with a phone call or through the website. The home page should inspire people to call us.

```html
<!DOCTYPE html>
<html lang="en">
<head>
<meta charset="utf-8">
<title>Willowmere Home Care</title>
<link href="https://fonts.googleapis.com/css2?family=Cinzel:wght@400;600;700&family=Jost:wght@400;500&display=swap" rel="stylesheet">
<style>
:root{
  --blue:#1a74c6;
  --blue-dark:#125fa8;
  --blue-light:#2aa3df;
  --footer:#1467b8;
  --footer-deep:#0f4f8e;
  --grey-text:#6c6c6c;
  --grey-line:#d6d6d6;
  --grey-bg:#f1f1f1;
  --dark-tab:#5a5a5a;
  --white:#fff;
}
*{box-sizing:border-box;margin:0;padding:0}
html,body{width:1200px;height:2378px;overflow:hidden;background:var(--white)}
body{position:relative;font-family:'Jost',sans-serif;color:var(--grey-text)}
.abs{position:absolute}

/* header */
.header{left:0;top:0;width:1200px;height:116px;background:linear-gradient(#fff,#f1f1f1)}
.brand{left:133px;top:34px;font-family:'Cinzel',serif;font-weight:700;font-size:31px;color:var(--blue);letter-spacing:.5px;white-space:nowrap}
.contact-today{left:822px;top:26px;font-family:'Cinzel',serif;font-weight:700;font-size:18px;color:var(--blue-dark)}
.head-phone{left:748px;top:62px;display:flex;align-items:center;gap:8px;font-size:19px;color:var(--grey-text)}
.quote-btn{left:925px;top:62px;width:143px;height:28px;display:flex;border-radius:3px;overflow:hidden}
.quote-btn span{flex:1;background:linear-gradient(#2fb0ec,#1b8fd4);color:#fff;font-family:'Cinzel',serif;font-size:11px;font-weight:600;display:flex;align-items:center;justify-content:center}
.quote-btn i,.cta-btn i{width:30px;background:var(--dark-tab);color:#fff;font-style:normal;display:flex;align-items:center;justify-content:center;font-size:14px}

/* nav */
.nav{left:0;top:116px;width:1200px;height:42px;background:linear-gradient(#2a86d6,#1566b6);display:flex;padding-left:133px}
.nav a{display:flex;align-items:center;justify-content:center;color:#fff;text-decoration:none;font-family:'Cinzel',serif;font-weight:600;font-size:15px;border-right:1px solid rgba(255,255,255,.25);padding:0 20px;white-space:nowrap}
.nav a.active{background:#7a7f85}

/* hero */
.hero{left:0;top:158px;width:1200px;height:570px;overflow:hidden}
.hero-photo{position:absolute;inset:0;background:linear-gradient(90deg,#0e140d 0%,#1f2e19 35%,#4a7232 58%,#7f9f58 76%,#5d7d3e 100%)}
.hero-copy{left:133px;top:172px;color:#fff}
.hero-copy h1{font-family:'Cinzel',serif;font-weight:700;font-size:30px;line-height:1.2}
.hero-copy h2{font-family:'Cinzel',serif;font-weight:600;font-size:24px;margin-top:4px}
.hero-copy hr{border:0;border-top:1px solid rgba(255,255,255,.6);width:225px;margin:16px 0 10px}
.hero-copy p{font-family:'Cinzel',serif;font-weight:600;font-size:17px}
.hero-phone{display:flex;align-items:center;gap:12px;margin-top:30px;font-size:31px;font-weight:500}
.hero-curve{left:0;top:680px}

/* sections */
.section-title{left:0;width:1200px;text-align:center;font-family:'Cinzel',serif;font-weight:700;font-size:31px;color:var(--blue-dark)}
.welcome-text{left:145px;top:855px;width:910px;text-align:center;font-size:12px;line-height:23px}

.call-label,.form-label{font-family:'Cinzel',serif;font-size:15px;color:var(--blue-light);top:1036px;white-space:nowrap}
.call-label{left:133px}
.form-label{left:530px}
.call-phone{left:133px;top:1062px;display:flex;align-items:center;gap:10px;font-size:30px}
.field{top:1066px;height:33px;border:1px solid #cfcfcf;background:#fff;font-size:11px;color:#555;padding:9px 12px}
.submit{left:958px;top:1066px;width:110px;height:33px;background:linear-gradient(#2b86d6,#1466b6);color:#fff;font-family:'Cinzel',serif;font-weight:700;font-size:12px;display:flex;align-items:center;justify-content:center;border-radius:2px}

.how-bg{left:0;top:1170px;width:1200px;height:580px}
.step{width:300px;text-align:center}
.step h3{font-family:'Cinzel',serif;font-weight:700;font-size:21px;color:var(--blue-dark);margin-top:10px;white-space:nowrap}
.step p{font-size:13px;line-height:21px;margin-top:8px;padding:0 70px}
.people-photo{left:528px;top:1565px;width:148px;height:128px;background:linear-gradient(#eef2f5,#c9cfd6);border-radius:4px}
.cta-btn{left:512px;top:1690px;width:176px;height:27px;display:flex;border-radius:14px;overflow:hidden}
.cta-btn span{flex:1;background:linear-gradient(#33b0ec,#1b8fd4);color:#fff;font-family:'Cinzel',serif;font-size:11px;font-weight:600;display:flex;align-items:center;justify-content:center}

.client-art{left:145px;top:1900px;width:170px;height:170px;border-radius:50%;background:radial-gradient(#bcd8ef,#2a8bd2)}
.quote{left:390px;top:1915px;width:670px;font-size:15px;line-height:28px;color:#555}
.qmark{font-family:Georgia,serif;font-size:60px;color:#c9c9c9;line-height:1}
.author{left:390px;top:2012px;font-family:'Cinzel',serif;font-weight:700;font-size:17px;color:var(--blue-dark);white-space:nowrap}
.author small{font-family:'Jost',sans-serif;font-weight:500;font-size:12px;color:var(--blue-light);margin-left:8px}
.arrow{top:1970px;font-size:38px;color:#c9c9c9;font-family:'Jost',sans-serif}

/* footer */
.footer{left:0;top:2135px;width:1200px;height:200px}
.follow{left:0;top:2168px;width:1200px;display:flex;justify-content:center;align-items:center;gap:7px;color:#fff;font-family:'Cinzel',serif;font-size:17px}
.follow b{font-weight:400;margin-right:6px}
.follow i{width:24px;height:24px;border-radius:50%;background:#fff;display:block}
.foot-brand{left:133px;top:2232px;font-family:'Cinzel',serif;font-weight:700;font-size:15px;color:#fff;white-space:nowrap}
.foot-copy{left:133px;top:2268px;font-family:'Cinzel',serif;font-weight:700;font-size:11px;color:#fff;line-height:18px;white-space:nowrap}
.foot-sep{top:2215px;width:1px;height:105px;background:rgba(255,255,255,.2)}
.foot-item{top:2218px;width:240px;text-align:center;color:#fff;font-size:15px;white-space:nowrap}
.foot-item .ic{width:50px;height:50px;border-radius:50%;background:var(--footer-deep);margin:0 auto 14px;display:flex;align-items:center;justify-content:center}
.bottom-nav{left:0;top:2335px;width:1200px;height:43px;display:flex;justify-content:space-between;align-items:center;padding:0 133px}
.bottom-nav a{font-family:'Cinzel',serif;font-size:14px;color:#555;text-decoration:none;white-space:nowrap}
</style>
</head>
<body>

<header class="abs header"></header>
<div class="abs brand">Willowmere Home Care</div>
<div class="abs contact-today">Contact Us Today!</div>
<div class="abs head-phone">
  <svg width="30" height="26" viewBox="0 0 30 26"><path d="M3 12 L15 2 L27 12 M6 10 V24 H24 V10" fill="none" stroke="#2aa3df" stroke-width="2.5"/><path d="M11 14 q4 -4 8 0 l-1 2 h-6z M10 17 h10 v4 h-10z" fill="#2aa3df"/></svg>
  <span>444-444-4444</span>
</div>
<div class="abs quote-btn"><span>GET A QUOTE</span><i>»</i></div>

<nav class="abs nav">
  <a class="active" href="#">Home</a>
  <a href="#">Services</a>
  <a href="#">Free In-Home Consultation</a>
  <a href="#">Client Portal</a>
  <a href="#">About Us ▾</a>
  <a href="#">Contact Us</a>
</nav>

<section class="abs hero">
  <div class="hero-photo" role="img" aria-label="Photo of a smiling caregiver kneeling beside an elderly woman in a wheelchair in a sunny garden"></div>
  <div class="abs hero-copy">
    <h1>Family-Owned,</h1>
    <h2>Service You Can Trust</h2>
    <hr>
    <p>Assisting the Maple Valley.</p>
    <div class="hero-phone">
      <svg width="40" height="36" viewBox="0 0 30 26"><path d="M3 12 L15 2 L27 12 M6 10 V24 H24 V10" fill="none" stroke="#2aa3df" stroke-width="2.5"/><path d="M11 14 q4 -4 8 0 l-1 2 h-6z M10 17 h10 v4 h-10z" fill="#fff"/></svg>
      <span>444-444-4444</span>
    </div>
  </div>
</section>
<svg class="abs hero-curve" width="1200" height="60" viewBox="0 0 1200 60">
  <path d="M0 40 Q600 -10 1200 40 V60 H0Z" fill="#fff"/>
  <path d="M0 42 Q600 -8 1200 42" fill="none" stroke="#d0d0d0" stroke-width="2"/>
</svg>

<h2 class="abs section-title" style="top:802px">Welcome to Willowmere Home Care</h2>
<p class="abs welcome-text">Willowmere Home Care is a local family owned and operated agency devoted to helping families like yours in the Maple Valley. We take pride in the relationships we develop with our clients. We understand this is a challenging time and we are dedicated to providing the peace of mind you deserve. At Willowmere Home Care we do more than just watch your loved ones. We care for them with programs designed to keep them both mentally and physically comfortable, happy and healthy. Being a family agency is what makes Willowmere Home Care special and sets us apart. We treat our caregivers as part of the family too. They are paid more than the average care giver and receive year round continuing education, exceeding state mandated minimum standards by miles.</p>

<svg class="abs" style="left:133px;top:995px" width="935" height="110" viewBox="0 0 935 110">
  <path d="M0 25 H270 L317 2 L364 25 H935" fill="none" stroke="#d6d6d6" stroke-width="1.5"/>
  <path d="M267 58 L317 22 L367 58 M278 50 V102 H356 V50" fill="none" stroke="#1a74c6" stroke-width="7" stroke-linejoin="miter"/>
  <text x="317" y="80" text-anchor="middle" font-family="Cinzel,serif" font-weight="700" font-size="20" fill="#6c6c6c">OR</text>
</svg>
<div class="abs call-label">Please call us directly at</div>
<div class="abs call-phone">
  <svg width="24" height="22" viewBox="0 0 24 22"><path d="M2 7 q10 -8 20 0 l-2 4 h-4 l-1 -3 h-6 l-1 3 h-4z M5 12 h14 v8 h-14z" fill="#1a74c6"/><circle cx="12" cy="16" r="2.5" fill="#fff"/></svg>
  <span>444-444-4444</span>
</div>
<div class="abs form-label">Click here to set up a free in-home consultation.</div>
<div class="abs field" style="left:530px;width:162px">Name</div>
<div class="abs field" style="left:700px;width:250px">E-mail Address</div>
<div class="abs submit">SUBMIT NOW</div>

<svg class="abs how-bg" width="1200" height="580" viewBox="0 0 1200 580">
  <path d="M0 40 Q600 -20 1200 40 V530 Q600 590 0 530Z" fill="#f0f0f0"/>
  <path d="M0 40 Q600 -20 1200 40" fill="none" stroke="#e3e3e3" stroke-width="2"/>
  <path d="M300 260 Q360 225 430 212" fill="none" stroke="#cfcfcf" stroke-dasharray="5 4" stroke-width="1.5"/>
  <path d="M765 212 Q840 225 900 260" fill="none" stroke="#cfcfcf" stroke-dasharray="5 4" stroke-width="1.5"/>
  <circle cx="392" cy="268" r="9" fill="#2aa3df"/><path d="M389 263 l5 5 -5 5" fill="none" stroke="#fff" stroke-width="2"/>
  <circle cx="815" cy="268" r="9" fill="#2aa3df"/><path d="M812 263 l5 5 -5 5" fill="none" stroke="#fff" stroke-width="2"/>
</svg>
<h2 class="abs section-title" style="top:1293px">How It Works</h2>

<div class="abs step" style="left:76px;top:1425px">
  <svg width="120" height="100" viewBox="0 0 120 100"><path d="M8 48 L60 6 L112 48 M20 40 V96 H100 V40" fill="none" stroke="#c4c4c4" stroke-width="7"/><circle cx="56" cy="58" r="10" fill="#2aa3df"/><path d="M38 90 q18 -22 36 0z" fill="#2aa3df"/><text x="78" y="56" font-family="Jost,sans-serif" font-weight="500" font-size="22" fill="#8a8a8a">?</text></svg>
  <h3>Describe Needs</h3>
  <p>Cras ultrices euism pharetra Suspendisse commodnis non tempus Pemroin lectus.</p>
</div>
<div class="abs step" style="left:450px;top:1352px">
  <svg width="120" height="100" viewBox="0 0 120 100"><path d="M8 48 L60 6 L112 48 M20 40 V96 H100 V40" fill="none" stroke="#c4c4c4" stroke-width="7"/><rect x="42" y="44" width="36" height="42" rx="3" fill="#2aa3df"/><rect x="52" y="40" width="16" height="8" fill="#1a74c6"/><path d="M50 66 l7 7 14 -14" fill="none" stroke="#fff" stroke-width="4"/></svg>
  <h3>Selact A Service</h3>
  <p>Cras ultrices euism pharetra Suspendisse commodnis non tempus Pemroin lectus.</p>
</div>
<div class="abs step" style="left:825px;top:1425px">
  <svg width="120" height="100" viewBox="0 0 120 100"><path d="M8 48 L60 6 L112 48 M20 40 V96 H100 V40" fill="none" stroke="#c4c4c4" stroke-width="7"/><path d="M36 52 h30 v20 h-18 l-8 7 v-7 h-4z" fill="#2aa3df"/><path d="M58 62 h28 v20 h-4 v7 l-8 -7 h-16z" fill="#1a74c6"/></svg>
  <h3>Stay Connected</h3>
  <p>Cras ultrices euism pharetra Suspendisse commodnis non tempus Pemroin lectus.</p>
</div>
<div class="abs people-photo" role="img" aria-label="Photo of a senior woman and her adult daughter standing together"></div>
<div class="abs cta-btn"><span>GET A CONCLUSION</span><i>»</i></div>

<h2 class="abs section-title" style="top:1843px">What Client Say About Us</h2>
<div class="abs client-art" role="img" aria-label="Illustration of a caring family figure framing a photo of a senior couple"></div>
<div class="abs qmark" style="left:352px;top:1895px">“</div>
<p class="abs quote">Morbi vehicula enim eget felis placerat pretium. Cras dignissim enim eget fringilla tincidunt. Praesent a dapibus leo, non fermentum purus. Maecenas at laoreet arcu. Etiam euismod hendrerit ant sodales mi vehicula quis. Donec lobortis fermentum dolor, ut tincidunt diam volutpat eu.</p>
<div class="abs qmark" style="left:918px;top:1975px">”</div>
<div class="abs author">Walter Brennick <small>(Retired Person)</small></div>
<div class="abs arrow" style="left:82px">‹</div>
<div class="abs arrow" style="left:1098px">›</div>

<svg class="abs footer" width="1200" height="200" viewBox="0 0 1200 200">
  <path d="M0 25 Q600 -15 1200 25 V200 H0Z" fill="#1467b8"/>
  <path d="M0 25 Q600 -15 1200 25" fill="none" stroke="#2aa3df" stroke-width="5"/>
</svg>
<div class="abs follow"><b>FOLLOW US ON</b><i></i><i></i><i></i><i></i></div>
<div class="abs foot-brand">Willowmere Home Care</div>
<div class="abs foot-copy">© 2016 WILLOWMERE HOME CARE.<br>ALL RIGHTS RESERVED</div>
<div class="abs foot-sep" style="left:355px"></div>
<div class="abs foot-sep" style="left:640px"></div>
<div class="abs foot-sep" style="left:880px"></div>
<div class="abs foot-item" style="left:378px">
  <div class="ic"><svg width="18" height="24" viewBox="0 0 18 24"><path d="M9 1 a8 8 0 0 1 8 8 c0 6 -8 14 -8 14 s-8 -8 -8 -14 a8 8 0 0 1 8 -8z" fill="#fff"/><circle cx="9" cy="9" r="3" fill="#0f4f8e"/></svg></div>
  Maple Valley , CA 95501
</div>
<div class="abs foot-item" style="left:620px">
  <div class="ic"><svg width="22" height="22" viewBox="0 0 22 22"><path d="M4 1 l5 5 -3 3 q3 5 7 7 l3 -3 5 5 -3 3 q-10 -1 -17 -17z" fill="#fff"/></svg></div>
  444-444-4444
</div>
<div class="abs foot-item" style="left:860px">
  <div class="ic"><svg width="24" height="18" viewBox="0 0 24 18"><rect x="1" y="1" width="22" height="16" fill="#fff"/><path d="M1 1 l11 9 11 -9" fill="none" stroke="#0f4f8e" stroke-width="2"/></svg></div>
  info@willowmerehomecare.com
</div>

<nav class="abs bottom-nav">
  <a href="#">Home</a>
  <a href="#">Services</a>
  <a href="#">Free In-Home Consultation</a>
  <a href="#">Client Portal</a>
  <a href="#">About Us</a>
  <a href="#">Contact Us</a>
</nav>

</body>
</html>
```